Best local air conditioning and heating contractor

We need a website design for a new company in Tampa Bay called the Summit Breeze Cooling Company. We provide superior services for residential and commercial properties as well as maintenance and installing HVAC systems. We also want to sell equipment, parts and filter on the website as well. We want it easy to use for customers. Rich with content and keywords for our area.

Target Market(s)

homeowners in Tampa Bay

Industry/Entity Type

HVAC air conditioning and heating

Coding

Coded - Design and coding required

Number of Pages Required

5+ page

Font styles to use
Sans Serif

Requirements
Nice to have
• would like the colors to be same as logo

```html
<!DOCTYPE html>
<html lang="en">
<head>
<meta charset="utf-8">
<title>Summit Breeze Cooling Company – Best Local Air Conditioning and Heating Contractor</title>
<link href="https://fonts.googleapis.com/css2?family=Oswald:wght@400;500;600;700&family=Poppins:ital,wght@0,400;0,500;0,600;1,400&display=swap" rel="stylesheet">
<style>
:root{
  --navy:#233477;
  --navy-deep:#1c2a63;
  --navy-line:#3a4c94;
  --red:#e02b2b;
  --white:#ffffff;
  --ink:#2b2b35;
  --muted:#4a4f63;
  --pale:#eef2f8;
  --placeholder-light:#eceef3;
  --placeholder-dark:#cfd3dd;
  --head:'Oswald',sans-serif;
  --body:'Poppins',sans-serif;
}
*{box-sizing:border-box;margin:0;padding:0}
html,body{width:1200px;height:3021px;overflow:hidden;background:var(--white)}
body{font-family:var(--body);color:var(--ink)}
.page{position:relative;width:1200px;height:3021px;overflow:hidden}
.abs{position:absolute}
a{text-decoration:none}
.brand{font-family:var(--head);font-weight:700;color:var(--navy);text-transform:uppercase;line-height:1;display:flex;align-items:center;gap:10px}
.brand-dot{width:16px;height:16px;border-radius:50%;background:var(--red);flex:none}
.brand-text span{display:block}
/* top bar */
.topbar{left:395px;top:0;width:720px;height:43px;background:var(--white);box-shadow:0 2px 8px rgba(0,0,0,.08);clip-path:polygon(18px 0,100% 0,100% 100%,0 100%);display:flex;align-items:center;font-family:var(--head);font-size:15px;color:var(--navy);font-weight:500}
.hours{display:flex;align-items:center;gap:10px;padding-left:34px;width:358px}
.socials{display:flex;gap:10px}
.social{width:19px;height:19px;border-radius:50%;background:var(--navy)}
.phone-tab{left:910px;top:0;width:205px;height:43px;background:var(--red);clip-path:polygon(22px 0,100% 0,calc(100% - 22px) 100%,0 100%);color:var(--white);font-family:var(--head);font-size:16px;display:flex;align-items:center;justify-content:center;gap:8px}
.nav{top:86px;left:458px;font-family:var(--head);font-size:18px;font-weight:500;color:var(--navy)}
.nav a{color:inherit;position:absolute;white-space:nowrap}
.nav-under{left:458px;top:139px;width:40px;height:4px;background:var(--red)}
/* hero */
.hero{left:0;top:143px;width:1200px;height:572px;background:var(--navy)}
.hero-title{left:85px;top:214px;font-family:var(--head);font-weight:600;font-size:55px;line-height:60px;color:var(--white);text-transform:uppercase;letter-spacing:.3px}
.hero-title em{font-style:normal;color:var(--red)}
.hero-lead{left:85px;top:346px;width:600px;font-size:15.5px;line-height:24px;color:var(--white)}
.btn{display:flex;align-items:center;justify-content:space-between;background:var(--red);color:var(--white);font-family:var(--head);font-weight:500;font-size:18px;text-transform:uppercase;padding:0 12px 0 16px}
.btn .arrow{width:22px;height:22px;flex:none}
.houses{left:0;top:470px;width:1200px;height:245px;background:linear-gradient(180deg,rgba(58,76,148,.25),rgba(58,76,148,.9))}
.vehicle{border-radius:14px;background:linear-gradient(180deg,var(--placeholder-light),var(--placeholder-dark))}
/* quote form */
.quote{left:841px;top:143px;width:274px;height:387px;background:var(--navy-deep)}
.quote-head{left:841px;top:143px;width:274px;height:82px;background:var(--red);clip-path:polygon(0 0,100% 0,100% 72%,50% 100%,0 72%);color:var(--white);font-family:var(--head);font-weight:600;font-size:21px;line-height:26px;text-align:center;padding-top:16px;text-transform:uppercase}
.field{left:862px;width:231px;height:39px;background:var(--white);font-family:var(--head);font-size:12px;font-weight:500;color:var(--navy);padding:12px 14px;text-transform:uppercase}
.quote-btn{left:862px;top:462px;width:231px;height:39px;background:var(--red);color:var(--white);font-family:var(--head);font-weight:500;font-size:18px;text-align:center;line-height:39px;text-transform:uppercase}
/* about */
.about-photo{left:87px;top:838px;width:470px;height:375px;background:linear-gradient(135deg,#8aa0b5,#2d5a59 55%,#c9b59a)}
.about-person{left:350px;top:795px;width:220px;height:330px;border-radius:100px 100px 0 0;background:linear-gradient(180deg,#c99a6a,#5b7fb6 45%,#7aa3cf)}
.badge{left:87px;top:838px;width:175px;height:89px;background:var(--red);color:var(--white);font-family:var(--head);font-size:23px;line-height:27px;padding:18px 0 0 27px;text-transform:uppercase}
.badge b{font-weight:600}
.video{left:413px;top:1124px;width:185px;height:89px;background:var(--white);box-shadow:0 6px 18px rgba(0,0,0,.12);display:flex;align-items:center;gap:14px;padding-left:22px;font-family:var(--head);font-size:16px;line-height:19px;text-transform:uppercase;color:var(--navy-deep)}
.video .play{width:46px;height:46px;border-radius:50%;background:var(--red);flex:none;display:flex;align-items:center;justify-content:center}
.video em{font-style:normal;color:var(--red);display:block}
.eyebrow{font-family:var(--head);font-size:17px;font-weight:500;color:var(--red);text-transform:uppercase}
.h2{font-family:var(--head);font-weight:600;font-size:40px;line-height:43px;color:var(--navy);text-transform:uppercase}
.about-copy{left:638px;top:973px;width:477px;font-size:14px;line-height:21.5px;text-align:justify;color:var(--muted)}
/* services */
.services{left:0;top:1301px;width:1200px;height:535px;background:var(--navy)}
.svc-ring{left:430px;top:1452px;width:342px;height:342px;border-radius:50%;border:2px solid #6d7fbf}
.svc-photo{left:450px;top:1472px;width:302px;height:302px;border-radius:50%;background:radial-gradient(circle,#f2f2f2,#b9b9b9)}
.svc-logo{left:450px;top:1590px;width:302px;justify-content:center;font-size:26px}
.ring-dot{width:15px;height:15px;border-radius:50%;background:var(--red)}
.svc-title{font-family:var(--body);font-weight:600;font-size:16px;line-height:19px;color:var(--white);text-transform:uppercase;letter-spacing:.5px}
.svc-text{font-size:12px;line-height:18.5px;color:#e4e8f6;margin-top:12px}
.svc-left{width:218px;text-align:right}
.svc-right{width:220px}
.svc-icon{width:90px;height:90px;border-radius:50%;border:2px solid #c9d1ee;display:flex;align-items:center;justify-content:center}
/* testimonials */
.testi-copy{left:85px;top:2087px;width:345px;font-size:13.5px;line-height:21px;color:var(--muted)}
.card{top:1952px;width:289px;height:253px;background:var(--white);border-radius:22px;box-shadow:0 6px 24px rgba(35,52,119,.12);padding:28px 30px}
.card::after{content:"";position:absolute;left:40px;bottom:-12px;width:24px;height:24px;background:var(--white);transform:rotate(45deg);box-shadow:6px 6px 10px rgba(35,52,119,.06)}
.qmark{font-family:var(--head);font-size:86px;line-height:60px;color:transparent;-webkit-text-stroke:2px var(--red);height:50px}
.card p{margin-top:24px;font-style:italic;font-size:12px;line-height:17px;text-align:justify;color:var(--navy-deep)}
.person{display:flex;align-items:center;gap:20px;top:2235px}
.avatar{width:58px;height:58px;border-radius:50%;background:linear-gradient(180deg,#d8d1c9,#a98f7b)}
.person b{display:block;font-weight:500;font-size:16px;color:var(--navy-deep)}
.person span{font-size:16px;color:var(--red)}
/* offer */
.offer{left:0;top:2395px;width:1200px;height:290px;background:var(--pale)}
.offer-photo{left:85px;top:2325px;width:430px;height:360px;background:linear-gradient(120deg,#e8e8e8 0%,#cfcfcf 40%,#2f8fdc 60%,#1f6fb5 100%)}
.offer-title{left:560px;top:2440px;width:565px;text-align:center;font-family:var(--head);font-weight:600;font-size:38px;line-height:42px;color:var(--navy);text-transform:uppercase}
.offer-sub{left:560px;top:2534px;width:565px;text-align:center;font-size:17px;line-height:24px;color:var(--red)}
/* footer */
.footer{left:0;top:2685px;width:1200px;height:336px;background:var(--navy)}
.fdiv{width:1px;height:170px;background:#6e7fc0;top:2735px}
.fhead{font-family:var(--body);font-weight:600;font-size:15px;color:var(--red);text-transform:uppercase}
.flist{font-size:14.5px;line-height:24px;color:var(--white);list-style:none}
.fcontact{font-size:14.5px;line-height:18px;color:var(--white);display:flex;gap:10px}
.fcontact svg{flex:none;margin-top:2px}
.map{left:900px;top:2768px;width:214px;height:137px;background:linear-gradient(135deg,#e9ede4,#d6dfe6);border:3px solid var(--white)}
.fsocial{width:27px;height:27px;border-radius:50%;border:2px solid var(--white)}
.copyright{left:0;top:2980px;width:1200px;text-align:center;font-size:13.5px;color:var(--white)}
.frule{left:0;top:2962px;width:1200px;height:1px;background:#34468b}
</style>
</head>
<body>
<div class="page">

  <!-- header -->
  <div class="abs brand" style="left:88px;top:42px;font-size:30px">
    <div class="brand-dot"></div>
    <div class="brand-text"><span>Summit Breeze</span><span>Cooling Company</span></div>
  </div>

  <div class="abs topbar">
    <div class="hours">
      <svg width="22" height="22" viewBox="0 0 22 22"><circle cx="11" cy="11" r="9" fill="none" stroke="#e02b2b" stroke-width="2"/><path d="M11 6v5l3 2" stroke="#e02b2b" stroke-width="2" fill="none" stroke-linecap="round"/></svg>
      MONDAY - SATURDAY : 9.00AM TO 6.30PM
    </div>
    <div class="socials"><span class="social"></span><span class="social"></span><span class="social"></span><span class="social"></span><span class="social"></span></div>
  </div>
  <div class="abs phone-tab">
    <svg width="17" height="17" viewBox="0 0 24 24"><circle cx="12" cy="12" r="11" fill="#fff"/><path d="M8 6l2 0 1 3-1.5 1a7 7 0 0 0 4.5 4.5l1-1.5 3 1v2a2 2 0 0 1-2 2A11 11 0 0 1 6 8a2 2 0 0 1 2-2z" fill="#e02b2b"/></svg>
    +1 727-555-0148
  </div>

  <nav class="abs nav">
    <a style="left:0">HOME</a>
    <a style="left:83px">ABOUT US</a>
    <a style="left:197px">OUR SERVICES</a>
    <a style="left:342px">TESTIMONIALS</a>
    <a style="left:484px">OFFER</a>
    <a style="left:570px">CONTACT US</a>
  </nav>
  <div class="abs nav-under"></div>

  <!-- hero -->
  <section class="abs hero"></section>
  <div class="abs houses" role="img" aria-label="Line illustration of a suburban street with houses, trees and a person walking a dog"></div>
  <h1 class="abs hero-title"><em>Best Local</em> Air Conditioning<br>and Heating Contractor</h1>
  <p class="abs hero-lead">Lorem Ipsum is simply dummy text of the printing and typesetting industry.<br>Lorem Ipsum has been the industry's standard dummy text.</p>
  <a class="abs btn" style="left:85px;top:413px;width:163px;height:44px">Contact Us
    <svg class="arrow" viewBox="0 0 22 22"><circle cx="11" cy="11" r="10" fill="#fff"/><path d="M6 11h9M11 7l4 4-4 4" stroke="#e02b2b" stroke-width="2.2" fill="none" stroke-linecap="round" stroke-linejoin="round"/></svg></a>
  <div class="abs vehicle" style="left:212px;top:583px;width:408px;height:150px" role="img" aria-label="Photo of the company service van"></div>

  <div class="abs quote"></div>
  <div class="abs quote-head">Start Here for a<br>Free Quote</div>
  <div class="abs field" style="top:257px">Name</div>
  <div class="abs field" style="top:308px">Pin Code</div>
  <div class="abs field" style="top:359px">Mobile Number</div>
  <div class="abs field" style="top:410px">Email</div>
  <div class="abs quote-btn">Get a Free Quote</div>

  <!-- about -->
  <div class="abs about-photo" role="img" aria-label="Outdoor air conditioning condenser unit"></div>
  <div class="abs about-person" role="img" aria-label="Smiling homeowner leaning on the condenser unit"></div>
  <div class="abs badge"><b>24 Years</b><br>of Experience</div>
  <div class="abs video">
    <div class="play"><svg width="16" height="18" viewBox="0 0 16 18"><path d="M2 1l13 8-13 8z" fill="#fff"/></svg></div>
    <div><em>Watch</em>Video Tour</div>
  </div>
  <div class="abs eyebrow" style="left:638px;top:838px">About Company</div>
  <h2 class="abs h2" style="left:638px;top:869px">Air Conditioning<br>and Heating Specialists</h2>
  <p class="abs about-copy">Lorem Ipsum is simply dummy text of the printing and typesetting industry. Lorem Ipsum has been the industry's standard dummy text ever since the 1500s, when an unknown printer took a galley of type and scrambled it to make a type specimen book. It has survived not only five centuries, but also the leap into electronic typesetting, remaining essentially unchanged. It was popularised in the 1960s with the release of Letraset sheets containing Lorem Ipsum passages, and more recently with desktop publishing software like</p>
  <a class="abs btn" style="left:638px;top:1168px;width:163px;height:43px">Read More
    <svg class="arrow" viewBox="0 0 22 22"><circle cx="11" cy="11" r="10" fill="#fff"/><path d="M6 11h9M11 7l4 4-4 4" stroke="#e02b2b" stroke-width="2.2" fill="none" stroke-linecap="round" stroke-linejoin="round"/></svg></a>

  <!-- services -->
  <section class="abs services"></section>
  <div class="abs eyebrow" style="left:0;top:1353px;width:1200px;text-align:center">Our Services</div>
  <h2 class="abs h2" style="left:0;top:1380px;width:1200px;text-align:center;color:var(--white)">Specialise Services</h2>
  <div class="abs svc-ring"></div>
  <div class="abs svc-photo" role="img" aria-label="Faded photo of an outdoor condenser unit"></div>
  <div class="abs brand svc-logo"><span>Summit Breeze Cooling</span></div>
  <div class="abs ring-dot" style="left:453px;top:1515px"></div>
  <div class="abs ring-dot" style="left:735px;top:1515px"></div>
  <div class="abs ring-dot" style="left:444px;top:1698px"></div>
  <div class="abs ring-dot" style="left:744px;top:1698px"></div>
  <div class="abs vehicle" style="left:438px;top:1725px;width:344px;height:130px" role="img" aria-label="Photo of the company service van"></div>

  <div class="abs svc-left" style="left:84px;top:1468px"><div class="svc-title">Air Conditioning &amp;<br>Heating Service</div><p class="svc-text">Lorem Ipsum is simply dummy text of the printing and typesetting industry. Lorem Ipsum has been the industry's standard dummy text.</p></div>
  <div class="abs svc-icon" style="left:322px;top:1464px"><svg width="46" height="40" viewBox="0 0 46 40" fill="none" stroke="#fff" stroke-width="2"><rect x="2" y="3" width="42" height="16" rx="2"/><path d="M6 14h34"/><circle cx="15" cy="29" r="7"/><path d="M15 22v14M8 29h14M30 26c2 2 2 4 0 6M36 26c2 2 2 4 0 6"/></svg></div>

  <div class="abs svc-left" style="left:84px;top:1665px"><div class="svc-title">Air Conditioning &amp;<br>Heating Repair</div><p class="svc-text">Lorem Ipsum is simply dummy text of the printing and typesetting industry. Lorem Ipsum has been the industry's standard dummy text.</p></div>
  <div class="abs svc-icon" style="left:322px;top:1660px"><svg width="46" height="44" viewBox="0 0 46 44" fill="none" stroke="#fff" stroke-width="2"><circle cx="23" cy="12" r="8"/><path d="M23 2v4M23 18v4M13 12h4M29 12h4"/><rect x="4" y="24" width="38" height="16" rx="2"/><path d="M8 34h30M10 29h8"/></svg></div>

  <div class="abs svc-icon" style="left:788px;top:1464px"><svg width="46" height="44" viewBox="0 0 46 44" fill="none" stroke="#fff" stroke-width="2"><rect x="4" y="22" width="38" height="16" rx="2"/><path d="M8 32h30M16 4v12M30 4v12M12 4h8M26 4h8M16 16h14"/></svg></div>
  <div class="abs svc-right" style="left:900px;top:1468px"><div class="svc-title">Air Conditioning &amp;<br>Installation</div><p class="svc-text">Lorem Ipsum is simply dummy text of the printing and typesetting industry. Lorem Ipsum has been the industry's standard dummy text.</p></div>

  <div class="abs svc-icon" style="left:788px;top:1660px"><svg width="46" height="46" viewBox="0 0 46 46" fill="none" stroke="#fff" stroke-width="2"><rect x="4" y="4" width="38" height="38" rx="2"/><circle cx="18" cy="26" r="10"/><path d="M18 16v20M8 26h20M32 10h6M32 16h6M32 22h6"/></svg></div>
  <div class="abs svc-right" style="left:900px;top:1665px"><div class="svc-title">HVAC<br>Maintenance</div><p class="svc-text">Lorem Ipsum is simply dummy text of the printing and typesetting industry. Lorem Ipsum has been the industry's standard dummy text.</p></div>

  <!-- testimonials -->
  <div class="abs eyebrow" style="left:85px;top:1950px">Testimonials</div>
  <h2 class="abs h2" style="left:85px;top:1983px">What They're Talking<br>About Company?</h2>
  <p class="abs testi-copy">Lorem Ipsum is simply dummy text of the printing and typesetting industry. Lorem Ipsum has been the industry's standard dummy text ever since the 1500s, when an unknown printer took a galley of type and scrambled it to make a type specimen book. It has survived not only five centuries</p>
  <a class="abs btn" style="left:87px;top:2243px;width:163px;height:44px">View All
    <svg class="arrow" viewBox="0 0 22 22"><circle cx="11" cy="11" r="10" fill="#fff"/><path d="M6 11h9M11 7l4 4-4 4" stroke="#e02b2b" stroke-width="2.2" fill="none" stroke-linecap="round" stroke-linejoin="round"/></svg></a>

  <div class="abs card" style="left:474px"><div class="qmark">&ldquo;</div><p>Lorem Ipsum is simply dummy text of the printing and typesetting industry. Lorem Ipsum has been the industry's standard dummy text ever since the 1500s, when an unknown printer took a galley of type and scrambled it to make a type specimen book.</p></div>
  <div class="abs card" style="left:786px"><div class="qmark">&ldquo;</div><p>Lorem Ipsum is simply dummy text of the printing and typesetting industry. Lorem Ipsum has been the industry's standard dummy text ever since the 1500s, when an unknown printer took a galley of type and scrambled it to make a type specimen book.</p></div>
  <div class="abs card" style="left:1100px;opacity:.45"><div class="qmark">&ldquo;</div><p>Lorem Ipsum is simply dummy text of the printing and typesetting industry. Lorem Ipsum has been the industry's standard dummy text ever since the 1500s, when an unknown printer took a galley of type and scrambled it to make a type specimen book.</p></div>

  <div class="abs person" style="left:506px"><div class="avatar" role="img" aria-label="Customer portrait"></div><div><b>Daniel Ortiz</b><span>Customer</span></div></div>
  <div class="abs person" style="left:818px"><div class="avatar" role="img" aria-label="Customer portrait"></div><div><b>Kelly Brooks</b><span>Customer</span></div></div>
  <div class="abs person" style="left:1132px;opacity:.45"><div class="avatar" role="img" aria-label="Customer portrait"></div></div>

  <!-- offer -->
  <section class="abs offer"></section>
  <div class="abs offer-photo" role="img" aria-label="Technician in blue cap checking an outdoor AC unit with pressure gauges"></div>
  <h2 class="abs offer-title">Buy 1 Year Preventive<br>Maintenance, Get 1 Year Free!</h2>
  <p class="abs offer-sub">Take advantage of this awesome offer at<br>www.summitbreezeair.com or Call 727-555-0148 today!</p>
  <a class="abs btn" style="left:744px;top:2600px;width:162px;height:43px">Read More
    <svg class="arrow" viewBox="0 0 22 22"><circle cx="11" cy="11" r="10" fill="#fff"/><path d="M6 11h9M11 7l4 4-4 4" stroke="#e02b2b" stroke-width="2.2" fill="none" stroke-linecap="round" stroke-linejoin="round"/></svg></a>

  <!-- footer -->
  <footer class="abs footer"></footer>
  <div class="abs brand" style="left:85px;top:2760px;font-size:32px;color:var(--white)">
    <div class="brand-dot"></div>
    <div class="brand-text"><span>Summit Breeze</span><span>Cooling Company</span></div>
  </div>
  <div class="abs" style="left:124px;top:2880px;display:flex;gap:16px">
    <span class="fsocial"></span><span class="fsocial"></span><span class="fsocial"></span><span class="fsocial"></span><span class="fsocial"></span>
  </div>
  <div class="abs fdiv" style="left:414px"></div>
  <div class="abs fdiv" style="left:601px"></div>
  <div class="abs fdiv" style="left:870px"></div>

  <div class="abs fhead" style="left:452px;top:2731px">Main Menu</div>
  <ul class="abs flist" style="left:452px;top:2761px">
    <li>Home</li><li>About Us</li><li>Our Services</li><li>Testimonials</li><li>Offer</li><li>Contact Us</li>
  </ul>

  <div class="abs fhead" style="left:636px;top:2731px">Contact Us</div>
  <div class="abs fcontact" style="left:636px;top:2773px;width:230px">
    <svg width="10" height="13" viewBox="0 0 10 13"><path d="M5 0a5 5 0 0 1 5 5c0 3-5 8-5 8S0 8 0 5a5 5 0 0 1 5-5z" fill="#fff"/><circle cx="5" cy="5" r="2" fill="#233477"/></svg>
    <span>4820 Bayshore Blvd, Suite 210<br>Tampa, FL 33611</span>
  </div>
  <div class="abs fcontact" style="left:634px;top:2830px">
    <svg width="12" height="12" viewBox="0 0 24 24"><path d="M6 2l4 0 2 5-3 2a12 12 0 0 0 6 6l2-3 5 2v4a3 3 0 0 1-3 3A19 19 0 0 1 3 5a3 3 0 0 1 3-3z" fill="#fff"/></svg>
    <span>Phone: +1 727-555-0148</span>
  </div>
  <div class="abs fcontact" style="left:634px;top:2868px">
    <svg width="12" height="10" viewBox="0 0 12 10"><rect x="0" y="0" width="12" height="10" rx="1" fill="#fff"/><path d="M0 1l6 5 6-5" stroke="#233477" stroke-width="1.2" fill="none"/></svg>
    <span>info@summitbreeze.com</span>
  </div>

  <div class="abs fhead" style="left:897px;top:2731px">Our Location</div>
  <div class="abs map" role="img" aria-label="Map showing the company location in Tampa Bay"></div>

  <div class="abs frule"></div>
  <p class="abs copyright">Copyright &copy; 2024 Summit Breeze Cooling Company &nbsp;| All Right Reserved</p>

</div>
</body>
</html>
```